Need 4 childhood cancer facts posters

Hello. I run a nonprofit in East Tennessee, USA that supports children with cancer and their families.

I need 4 poster designs with facts about childhood cancers. It should either have pictures of children with cancer or be focused around the whole idea of childhood cancer awareness. This project will require time and research. I will post links to facts as the project goes forward.

Questions can be emailed to tmerrow@glowwithnora.org. AI format of our logo has been uploaded. I have images and links here http://www.glowwithnora.org/contest-pics.html

You can also view our website at www.glowwithnora.org

Some facts: http://pelt.tumorstats.example/archive/publications/childhood/

USE THESE FACTS: * Everyday, approximately 250 children will die from childhood cancer. *Childhood Cancers is the number 1 cause of death in children under age 15 in the US. *Less than 5% of the federal governments budget toward cancer research is dedicated to childhood cancers. *One in 330 children will be diagnosed with cancer by the time they are 20.

Poster will be 24 inches wide by 36 inches tall.

```html
<!DOCTYPE html>
<html lang="en">
<head>
<meta charset="utf-8">
<title>Childhood Cancer Facts Poster</title>
<link href="https://fonts.googleapis.com/css2?family=Amatic+SC:wght@700&family=Dancing+Script:wght@700&family=Londrina+Outline&family=Oswald:wght@500&display=swap" rel="stylesheet">
<style>
  :root {
    --sun: #f6cf45;
    --paper: #ffffff;
    --ink: #4a4a4a;
    --red: #e0483e;
    --olive: #c7b532;
    --green: #8fbf3f;
    --dot: #e8a19a;
  }
  html, body { margin: 0; padding: 0; overflow: hidden; }
  .poster {
    position: relative; width: 851px; height: 1200px; overflow: hidden;
    background: var(--sun); font-family: 'Oswald', sans-serif; color: var(--ink);
  }
  .poster > * { position: absolute; margin: 0; }
  .title {
    left: 135px; top: 50px; font-family: 'Dancing Script', cursive;
    font-size: 86px; line-height: 1; color: var(--ink); white-space: nowrap;
  }
  .panel { left: 58px; top: 250px; width: 735px; height: 910px; background: var(--paper); }
  .kids-art {
    left: 18px; top: 165px; width: 120px; height: 110px; border-radius: 40px;
    background: linear-gradient(90deg, #f2a65a, #f4e04d, #9ccf6a);
  }
  .divider-v { left: 410px; top: 275px; width: 0; height: 865px; border-left: 4px dotted var(--dot); }
  .divider-h { left: 75px; top: 680px; width: 700px; height: 0; border-top: 4px dotted var(--dot); }
  .label { font-family: 'Amatic SC', sans-serif; font-weight: 700; line-height: 1; letter-spacing: 2px; white-space: nowrap; }
  .small { font-family: 'Dancing Script', cursive; font-size: 20px; line-height: 1; }
  .figure { font-family: 'Londrina Outline', sans-serif; line-height: 1; }
  .fact-line { font-size: 30px; line-height: 1.1; letter-spacing: 1px; text-transform: uppercase; }

  .daily-heading { left: 85px; top: 328px; font-size: 80px; color: var(--olive); }
  .daily-around { left: 140px; top: 405px; }
  .daily-figure { left: 80px; top: 415px; font-size: 155px; color: var(--red); }
  .daily-text { left: 88px; top: 585px; color: var(--red); }

  .rank-heading { left: 440px; top: 290px; font-size: 46px; color: var(--ink); }
  .rank-are { left: 705px; top: 342px; }
  .rank-figure { left: 440px; top: 360px; font-size: 145px; color: var(--olive); }
  .rank-text { left: 442px; top: 540px; font-size: 28px; }

  .budget-heading { left: 85px; top: 712px; font-size: 74px; color: var(--green); }
  .budget-figure { left: 80px; top: 795px; font-size: 150px; color: var(--green); }
  .budget-of { left: 85px; top: 1010px; }
  .budget-text { left: 140px; top: 1003px; font-size: 25px; color: var(--green); }

  .odds-heading { left: 495px; top: 712px; font-size: 58px; color: var(--ink); }
  .odds-figure { left: 445px; top: 770px; font-size: 140px; color: var(--olive); }
  .odds-text { left: 442px; top: 925px; font-size: 26px; }
  .odds-with { left: 442px; top: 985px; }
  .odds-cancer { left: 490px; top: 958px; font-size: 84px; color: var(--red); }
  .odds-end { left: 442px; top: 1050px; font-size: 26px; }

  .brand { left: 442px; top: 1098px; display: flex; align-items: center; gap: 8px; }
  .brand-dot { width: 16px; height: 16px; border-radius: 50%; background: var(--olive); }
  .brand-name { font-family: 'Amatic SC', sans-serif; font-weight: 700; font-size: 19px; color: var(--ink); line-height: 1; width: 160px; }

  .toys-art {
    left: 708px; top: 1045px; width: 138px; height: 115px; border-radius: 50% 50% 20px 20px;
    background: linear-gradient(160deg, #f4dc8a, #e9c35a);
  }
  .footer {
    left: 0; top: 1170px; width: 851px; text-align: center;
    font-size: 14px; letter-spacing: 1px; color: var(--ink); line-height: 1;
  }
  .base-band { left: 0; top: 1192px; width: 851px; height: 8px; background: var(--red); }
</style>
</head>
<body>
<div class="poster">
  <h1 class="title">Childhood Cancer</h1>
  <div class="panel"></div>
  <div class="kids-art" role="img" aria-label="Illustration of three smiling cartoon children standing together"></div>

  <div class="divider-v"></div>
  <div class="divider-h"></div>

  <p class="label daily-heading">EVERYDAY</p>
  <p class="small daily-around">around</p>
  <p class="figure daily-figure">250</p>
  <p class="label fact-line daily-text">Children will die from<br>childhood cancer</p>

  <p class="label rank-heading">CHILDHOOD CANCERS</p>
  <p class="small rank-are">are the</p>
  <p class="figure rank-figure">NO.1</p>
  <p class="label fact-line rank-text">Cause of death in children<br>under age 15 in the US</p>

  <p class="label budget-heading">LESS THAN</p>
  <p class="figure budget-figure">5%</p>
  <p class="small budget-of">of the</p>
  <p class="label fact-line budget-text">Federal governments<br>budget toward<br>cancer research<br>is dedicated to<br>childhood cancers</p>

  <p class="label odds-heading">ONE IN</p>
  <p class="figure odds-figure">330</p>
  <p class="label fact-line odds-text">Children will be diagnosed</p>
  <p class="small odds-with">with</p>
  <p class="label odds-cancer">CANCER</p>
  <p class="label fact-line odds-end">By the time they are 20</p>

  <div class="brand">
    <span class="brand-dot"></span>
    <span class="brand-name">Nora Glenn Childhood Cancer Foundation</span>
  </div>

  <div class="toys-art" role="img" aria-label="Illustration of a teddy bear beside a toy truck"></div>

  <p class="footer">ALL DONATIONS GRATEFULLY RECEIVED, PLEASE VISIT WWW.GLOWWITHNORA.ORG</p>
  <div class="base-band"></div>
</div>
</body>
</html>
```